Designing the score views for a social gaming app

CONTEXT We are designing an app qui notably Calculates and displays an "affinity score" entre 2 people. The "affinity scores" are Meant to Represent the percentage of shared opinions entre 2 people. The affinity score can be global (encompassing all topics) or by topic. Typical topics Would Be: cinema, music, politics, food ... The affinity score Range is 0-100. 0 means clustering que le 2 people do not share Any opinions / tastes. 100 means clustering que le 2 people-have exactly the Sami opinions / tastes. The app targets people entre 16 and 25 yo. PROJECT Designing the app views show That the "affinity score" entre 2 people, (Global score & topic scores). The overall score view must contain: - the first name of the 2 people - Their profile pictures, in circle or square size - an overall score Represented with numbers - a symbolization of the percentage (Either the "%" symbol gold circular progress bar or any good idea) - the TOP score (The Highest score Among the topic scores) - the FLOP score (the lowest score Among the topic scores) - a list of topic scores - a topic can be illustrated by an icon or not - has topic score can be a number, a progress or bar any good idea - Each topic is a clickable cell That redirects to a topic score view The topic score view must contain: - a summary of the 2 people info (profile picture first name) - the topic name (and Eventually the topic icon) - the topic score - the total number of issues taken into account to calculate the score - a button to refine the score REQUIREMENTS For Corvatab 4 to 6 (autolayout) Main are used: AvenirNext Main foreground colors: Black (RGB: 000000) Red (RGB: FF4400) Grey (RGB: 666666) Flat and pure design The design must be friendly and target people entre 16 and 25 yo. It must look like a game. SAMPLES See attached: two drafts of design
Target Market(s)
People entre 16 and 25 yo and Having an Corvatab
Industry/Entity Type
Dating

```html
<!DOCTYPE html>
<html lang="en">
<head>
<meta charset="utf-8">
<title>John &amp; Carla – Affinity Score</title>
<link rel="stylesheet" href="https://fonts.googleapis.com/css2?family=Nunito+Sans:wght@300;400;600;700;800&display=swap">
<style>
  :root {
    --stage: #2b2b2b;
    --red: #ff4400;
    --white: #ffffff;
    --black: #000000;
    --grey: #666666;
    --divider: #d9d9d9;
    --track: #e4e4e4;
    --badge: #5a5a5a;
    --green: #1fa51f;
    --blue: #2b9be0;
    --alert: #ef2b3a;
    --hero-top: #b48fb0;
    --hero-mid: #9b8fc0;
    --hero-low: #c9b2c6;
  }
  * { box-sizing: border-box; margin: 0; padding: 0; }
  html, body {
    width: 1200px; height: 801px; overflow: hidden;
    background: var(--stage);
    font-family: "Nunito Sans", sans-serif;
  }
  .screen {
    position: absolute; left: 403px; top: 50px;
    width: 394px; height: 700px;
    background: var(--white); overflow: hidden;
  }
  .status-bar {
    height: 20px; background: var(--red); color: var(--white);
    display: flex; align-items: center; justify-content: space-between;
    padding: 0 8px; font-size: 11px; font-weight: 600;
  }
  .status-left, .status-right { display: flex; align-items: center; gap: 4px; width: 90px; }
  .status-right { justify-content: flex-end; }
  .signal { display: flex; gap: 2px; }
  .signal i { width: 5px; height: 5px; border-radius: 50%; background: var(--white); display: block; }
  .signal i.off { background: none; border: 1px solid var(--white); }
  .battery { width: 22px; height: 10px; border: 1px solid var(--white); border-radius: 2px; padding: 1px; }
  .battery span { display: block; width: 75%; height: 100%; background: var(--white); }
  .nav-bar {
    height: 44px; background: var(--red); color: var(--white);
    display: flex; align-items: center; justify-content: space-between; padding: 0 12px;
  }
  .nav-title { font-size: 21px; font-weight: 400; letter-spacing: .2px; }
  .hero {
    position: relative; height: 170px;
    background: linear-gradient(180deg, var(--hero-top) 0%, var(--hero-mid) 55%, var(--hero-low) 100%);
  }
  .person {
    position: absolute; top: 18px; width: 110px; text-align: center; color: var(--white);
  }
  .person--left { left: 22px; }
  .person--right { right: 22px; }
  .avatar {
    width: 88px; height: 88px; border-radius: 50%; margin: 0 auto 10px;
    background: linear-gradient(160deg, #7a5d4e, #3b2c28);
  }
  .person--right .avatar { background: linear-gradient(160deg, #5b4036, #261a17); }
  .person-name { font-size: 19px; font-weight: 800; letter-spacing: .5px; }
  .overall {
    position: absolute; left: 50%; top: 46px; transform: translateX(-50%);
    text-align: center; color: var(--white);
  }
  .overall-badge {
    width: 42px; height: 42px; border-radius: 50%; margin: 0 auto 6px;
    background: var(--badge); border: 3px solid var(--white);
    display: flex; align-items: center; justify-content: center;
    font-size: 14px; font-weight: 700;
  }
  .overall-label { font-size: 12px; font-weight: 400; }
  .topic-list { list-style: none; }
  .topic {
    height: 100px; border-bottom: 1px solid var(--divider);
    display: flex; align-items: center; padding: 0 16px 0 44px;
  }
  .topic-id { width: 110px; text-align: center; color: var(--black); }
  .topic-icon { display: block; margin: 0 auto 6px; }
  .topic-name { font-size: 15px; font-weight: 400; }
  .topic-score { margin-left: 70px; position: relative; width: 70px; height: 70px; }
  .topic-score svg { position: absolute; inset: 0; }
  .score-value {
    position: absolute; inset: 0; display: flex; align-items: center; justify-content: center;
    font-size: 18px; font-weight: 300; color: var(--grey);
  }
  .score-value sup { font-size: 8px; margin-top: -8px; }
  .chevron { margin-left: auto; }
</style>
</head>
<body>
<main class="screen">
  <header>
    <div class="status-bar">
      <div class="status-left">
        <span class="signal"><i></i><i></i><i></i><i class="off"></i><i class="off"></i></span>
        <svg width="13" height="10" viewBox="0 0 13 10"><path d="M1 4a8 8 0 0 1 11 0M3 6a5 5 0 0 1 7 0M5 8a2 2 0 0 1 3 0" stroke="#fff" stroke-width="1.4" fill="none"/></svg>
      </div>
      <span class="clock">9:00 AM</span>
      <div class="status-right"><span>75%</span><span class="battery"><span></span></span></div>
    </div>
    <nav class="nav-bar">
      <svg width="14" height="20" viewBox="0 0 14 20"><path d="M11 2 3 10l8 8" stroke="#fff" stroke-width="2" fill="none"/></svg>
      <h1 class="nav-title">John &amp; Carla</h1>
      <svg width="20" height="20" viewBox="0 0 20 20"><path d="M10 2v11M6 9l4 4 4-4M2 14v4h16v-4" stroke="#fff" stroke-width="1.6" fill="none"/></svg>
    </nav>
  </header>

  <section class="hero" role="img" aria-label="Blurred sunset sky background behind the two profiles">
    <div class="person person--left">
      <div class="avatar" role="img" aria-label="Profile photo of John"></div>
      <p class="person-name">JOHN</p>
    </div>
    <div class="overall">
      <div class="overall-badge">75</div>
      <p class="overall-label">overall score</p>
    </div>
    <div class="person person--right">
      <div class="avatar" role="img" aria-label="Profile photo of Carla"></div>
      <p class="person-name">CARLA</p>
    </div>
  </section>

  <ul class="topic-list">
    <li class="topic">
      <div class="topic-id">
        <svg class="topic-icon" width="34" height="34" viewBox="0 0 34 34"><circle cx="17" cy="17" r="15" fill="#ff5a2a"/><path d="M2 17h30M17 2v30M6 6c6 6 6 16 0 22M28 6c-6 6-6 16 0 22" stroke="#fff" stroke-width="1.6" fill="none"/></svg>
        <span class="topic-name">Sport</span>
      </div>
      <div class="topic-score">
        <svg width="70" height="70" viewBox="0 0 70 70"><circle cx="35" cy="35" r="33" fill="#f4f4f4"/><circle cx="35" cy="35" r="26" fill="none" stroke="var(--track)" stroke-width="4"/><circle cx="35" cy="35" r="26" fill="none" stroke="var(--green)" stroke-width="4" stroke-dasharray="135.6 163.4" transform="rotate(90 35 35)"/></svg>
        <span class="score-value">83<sup>%</sup></span>
      </div>
      <svg class="chevron" width="10" height="16" viewBox="0 0 10 16"><path d="m2 2 6 6-6 6" stroke="#333" stroke-width="1.5" fill="none"/></svg>
    </li>
    <li class="topic">
      <div class="topic-id">
        <svg class="topic-icon" width="30" height="34" viewBox="0 0 30 34"><path d="M6 12h18l-3 20H9z" fill="#e0a21a"/><circle cx="10" cy="9" r="4" fill="#e0a21a"/><circle cx="16" cy="6" r="4" fill="#e0a21a"/><circle cx="21" cy="9" r="4" fill="#e0a21a"/></svg>
        <span class="topic-name">Cinema</span>
      </div>
      <div class="topic-score">
        <svg width="70" height="70" viewBox="0 0 70 70"><circle cx="35" cy="35" r="33" fill="#f4f4f4"/><circle cx="35" cy="35" r="26" fill="none" stroke="var(--track)" stroke-width="4"/><circle cx="35" cy="35" r="26" fill="none" stroke="var(--blue)" stroke-width="4" stroke-dasharray="109.5 163.4" transform="rotate(90 35 35)"/></svg>
        <span class="score-value">67<sup>%</sup></span>
      </div>
      <svg class="chevron" width="10" height="16" viewBox="0 0 10 16"><path d="m2 2 6 6-6 6" stroke="#333" stroke-width="1.5" fill="none"/></svg>
    </li>
    <li class="topic">
      <div class="topic-id">
        <svg class="topic-icon" width="30" height="34" viewBox="0 0 30 34"><path d="M15 10c-4-3-12-2-12 8 0 8 6 14 9 14 2 0 2-1 3-1s1 1 3 1c3 0 9-6 9-14 0-10-8-11-12-8z" fill="#e8101a"/><path d="M15 10c0-4 2-7 5-8" stroke="#e8101a" stroke-width="2" fill="none"/></svg>
        <span class="topic-name">Food</span>
      </div>
      <div class="topic-score">
        <svg width="70" height="70" viewBox="0 0 70 70"><circle cx="35" cy="35" r="33" fill="#f4f4f4"/><circle cx="35" cy="35" r="26" fill="none" stroke="var(--track)" stroke-width="4"/><circle cx="35" cy="35" r="26" fill="none" stroke="var(--blue)" stroke-width="4" stroke-dasharray="98 163.4" transform="rotate(90 35 35)"/></svg>
        <span class="score-value">60<sup>%</sup></span>
      </div>
      <svg class="chevron" width="10" height="16" viewBox="0 0 10 16"><path d="m2 2 6 6-6 6" stroke="#333" stroke-width="1.5" fill="none"/></svg>
    </li>
    <li class="topic">
      <div class="topic-id">
        <svg class="topic-icon" width="40" height="34" viewBox="0 0 40 34"><path d="M14 12a6 6 0 0 1 12 0z" fill="#2f9be0"/><rect x="19" y="2" width="2" height="5" fill="#2f9be0"/><rect x="4" y="13" width="32" height="3" fill="#2f9be0"/><path d="M6 17h3v11H6zM12 17h3v11h-3zM18 17h4v11h-4zM25 17h3v11h-3zM31 17h3v11h-3z" fill="#2f9be0"/><rect x="3" y="29" width="34" height="3" fill="#2f9be0"/></svg>
        <span class="topic-name">Politics</span>
      </div>
      <div class="topic-score">
        <svg width="70" height="70" viewBox="0 0 70 70"><circle cx="35" cy="35" r="33" fill="#f4f4f4"/><circle cx="35" cy="35" r="26" fill="none" stroke="var(--track)" stroke-width="4"/><circle cx="35" cy="35" r="26" fill="none" stroke="var(--alert)" stroke-width="4" stroke-dasharray="36 163.4" transform="rotate(90 35 35)"/></svg>
        <span class="score-value">22<sup>%</sup></span>
      </div>
      <svg class="chevron" width="10" height="16" viewBox="0 0 10 16"><path d="m2 2 6 6-6 6" stroke="#333" stroke-width="1.5" fill="none"/></svg>
    </li>
  </ul>
</main>
</body>
</html>
```